Family owned plumbing contractor needs eye catching business card design

Business cards that are unique, eye catching, and provide customers with general company information, such as name, address, phone number, website, employee name/title, cell phone #, & email address. We are transitioning to a new logo that utilizes a more retro feel, so we are interested in seeing some cool old school designs in the mix. We are liking the dark background on some of the samples on this website. If that is workable with our artwork, we would like to see that incorporated into the design.
Contact Information for Business Card
Copperline Pipeworks, Inc.
www.copperlinepipeworks.example
(555) 392-7068 phone
Nevada License #64205
California License #5810473
Dale Wrennick, President
(555) 618-9032 cell
dale@copperlinepipeworks.example
Residential * Commercial * Service
Requirements
Must have
- The business card details listed above & logo provided.
Nice to have
- I made some notes about color options in the description.

```html
<!DOCTYPE html>
<html lang="en">
<head>
<meta charset="utf-8">
<title>Copperline Pipeworks – Business Card</title>
<link rel="stylesheet" href="https://fonts.googleapis.com/css2?family=Lato:ital,wght@0,400;0,700;1,400&display=swap">
<style>
  :root {
    --page: #e4e6e8;
    --card-white: #f4f5f5;
    --steel-blue: #4d7594;
    --steel-blue-light: #7fa4bf;
    --steel-blue-dark: #56798f;
    --teal: #5fbea6;
    --ink-grey: #777c80;
    --text-grey: #5e6468;
    --white: #ffffff;
  }
  * { box-sizing: border-box; margin: 0; padding: 0; }
  html, body { width: 1200px; height: 900px; overflow: hidden; }
  body {
    background: var(--page);
    font-family: "Lato", sans-serif;
    position: relative;
  }
  .card {
    position: absolute;
    left: 250px;
    width: 700px;
    height: 400px;
    border-radius: 28px;
    overflow: hidden;
    box-shadow: 0 6px 18px rgba(0,0,0,0.12);
  }

  /* Back side */
  .card-back { top: 30px; }
  .card-back .texture {
    position: absolute; inset: 0;
    background: radial-gradient(ellipse at 62% 35%, var(--steel-blue-light) 0%, var(--steel-blue-dark) 75%);
  }
  .brand-mark {
    position: absolute;
    display: flex; align-items: center; gap: 14px;
    font-weight: 700;
  }
  .card-back .brand-mark {
    left: 50%; top: 150px; transform: translateX(-50%);
    color: var(--white); font-size: 34px;
    white-space: nowrap;
  }
  .brand-dot {
    width: 30px; height: 30px; border-radius: 50%;
    background: var(--teal); flex: none;
  }
  .services {
    position: absolute; left: 0; right: 0; top: 300px;
    text-align: center; color: #e6eef4;
    font-size: 17px; letter-spacing: 0.5px;
  }
  .services .sep { margin: 0 8px; color: var(--white); }

  /* Front side */
  .card-front { top: 470px; background: var(--card-white); }
  .person { position: absolute; left: 88px; top: 58px; }
  .person-name { color: var(--steel-blue); font-weight: 700; font-size: 27px; }
  .person-title { color: var(--ink-grey); font-style: italic; font-size: 17px; margin-top: -2px; }
  .divider {
    position: absolute; left: 88px; top: 140px;
    width: 34px; height: 3px; background: var(--steel-blue);
  }
  .contact { position: absolute; left: 66px; top: 170px; }
  .company { color: var(--steel-blue); font-weight: 700; font-size: 18px; margin-left: 22px; margin-bottom: 4px; }
  .contact-row {
    display: flex; align-items: center; gap: 8px;
    color: var(--text-grey); font-size: 17px; line-height: 25px;
  }
  .contact-row svg { width: 14px; height: 14px; flex: none; }
  .card-front .brand-mark {
    left: 420px; top: 118px; width: 240px;
    color: var(--steel-blue); font-size: 26px; line-height: 1.25;
  }
  .license {
    position: absolute; top: 318px; height: 46px;
    color: var(--white); font-weight: 700; font-size: 18px;
    display: flex; align-items: center;
  }
  .license-nv { left: 0; width: 322px; background: var(--steel-blue); padding-left: 58px; }
  .license-ca { left: 330px; right: 0; background: var(--teal); justify-content: center; }
</style>
</head>
<body>

  <section class="card card-back" aria-label="Card back">
    <div class="texture" role="img" aria-label="Weathered steel-blue crackle texture background"></div>
    <div class="brand-mark"><span class="brand-dot"></span>Copperline Pipeworks, Inc.</div>
    <p class="services">Residential<span class="sep">✱</span>Commercial<span class="sep">✱</span>Service</p>
  </section>

  <section class="card card-front" aria-label="Card front">
    <div class="person">
      <p class="person-name">Dale Wrennick</p>
      <p class="person-title">President</p>
    </div>
    <div class="divider"></div>

    <div class="contact">
      <p class="company">Copperline Pipeworks, Inc.</p>
      <p class="contact-row">
        <svg viewBox="0 0 16 16" fill="none" stroke="#5e6468" stroke-width="1.4"><path d="M3 2l3 0 1 3-2 1.5a9 9 0 0 0 4.5 4.5L11 9l3 1v3c0 1-1 1.5-2 1.5A11 11 0 0 1 1.5 4C1.5 3 2 2 3 2z"/></svg>
        (555) 392-7068
      </p>
      <p class="contact-row">
        <svg viewBox="0 0 16 16" fill="none" stroke="#5e6468" stroke-width="1.4"><rect x="4" y="1.5" width="8" height="13" rx="1.5"/><line x1="7" y1="12" x2="9" y2="12"/></svg>
        (555) 618-9032
      </p>
      <p class="contact-row">
        <svg viewBox="0 0 16 16" fill="none" stroke="#5e6468" stroke-width="1.4"><rect x="1.5" y="3.5" width="13" height="9"/><path d="M1.5 3.5l6.5 5 6.5-5"/></svg>
        dale@copperlinepipeworks.example
      </p>
      <p class="contact-row">
        <svg viewBox="0 0 16 16" fill="none" stroke="#5e6468" stroke-width="1.3"><circle cx="8" cy="8" r="6.5"/><ellipse cx="8" cy="8" rx="3" ry="6.5"/><line x1="1.5" y1="8" x2="14.5" y2="8"/></svg>
        www.copperlinepipeworks.example
      </p>
    </div>

    <div class="brand-mark"><span class="brand-dot"></span><span>Copperline Pipeworks, Inc.</span></div>

    <div class="license license-nv">Nevada License #64205</div>
    <div class="license license-ca">California License #5810473</div>
  </section>

</body>
</html>
```